Website for IT consulting Company

I need a website upgrade, the existing site content is ok, I would also like to add a testimonial page, the site should be something that is easy for us to update content. You use the content from www.velmarketa.com as an example. I will also post update logo and artwork. I also need a contact form with some type of validation or captcha.

Please omit Address maps

Target Market(s)

small business, service oriented companies. We provide IT Consulting, support and mangement

Industry/Entity Type

Information Technology

Coding

Coded - Design and coding required

Number of Pages Required

1 page

Font styles to use
Serif
Sans Serif

Requirements
Must have
• Contain logo attached, and content from existing web site www.velmarketa.com.
• Also need to update content easily, and be movable to different platforms.
• There is a catch phrase
• "Let us worry about your technology…” “ so you don’t have to!”
• Should be included.
Nice to have
• Testimonial page, Project page where we can post new and past projects and pictures
Should not have
• none

```html
<!DOCTYPE html>
<html lang="en">
<head>
<meta charset="utf-8">
<title>Velmarketa Group – IT Consulting</title>
<link rel="stylesheet" href="https://fonts.googleapis.com/css2?family=Montserrat:wght@400;500;600;700&family=Open+Sans:ital,wght@0,400;0,600;1,400&display=swap">
<style>
:root{
  --blue:#1d95d9;
  --blue-dark:#1677c2;
  --navy:#0b1e3c;
  --orange:#f07b1e;
  --text:#8a8a8a;
  --ink:#444;
  --light:#f3f3f3;
  --white:#fff;
  --line:#d6d6d6;
}
*{box-sizing:border-box;margin:0;padding:0}
html,body{width:1200px;height:3125px;overflow:hidden}
body{font-family:"Open Sans",Arial,sans-serif;color:var(--ink);background:var(--white);position:relative}
section,header,footer{position:absolute;left:0;width:1200px}
.abs{position:absolute}

/* hero */
.hero{top:0;height:622px;background:radial-gradient(ellipse at 70% 55%,#2f6fb5 0%,#163f7a 35%,#0a1f40 75%,#06142a 100%);overflow:hidden}
.hero-photo{position:absolute;inset:0;background:linear-gradient(110deg,rgba(20,60,120,.0) 40%,rgba(220,190,170,.35) 70%,rgba(240,210,190,.45) 85%,rgba(20,60,120,.1) 100%)}
.brand{position:absolute;left:132px;top:36px;display:flex;align-items:center;gap:12px;font-family:"Montserrat",sans-serif;font-weight:700;font-size:34px;color:var(--white);letter-spacing:1px}
.brand-mark{width:26px;height:26px;background:var(--orange)}
.menu-toggle{position:absolute;left:964px;top:42px;display:flex;align-items:center;gap:10px;color:var(--white);font-family:"Montserrat",sans-serif;font-size:15px;font-weight:500}
.menu-toggle svg{display:block}
.nav-drop{position:absolute;left:848px;top:90px;width:219px;background:var(--blue);list-style:none}
.nav-drop::before{content:"";position:absolute;right:20px;top:-9px;border:9px solid transparent;border-top:0;border-bottom-color:var(--blue)}
.nav-drop li{height:37.5px;line-height:37.5px;padding-left:24px;font-family:"Montserrat",sans-serif;font-size:13px;color:var(--white);border-bottom:1px solid rgba(255,255,255,.25);position:relative}
.nav-drop li:last-child{border-bottom:0}
.nav-drop .has-sub::after{content:"›";position:absolute;right:12px;font-size:20px}
.hero-title{position:absolute;left:0;width:1200px;top:252px;text-align:center;font-family:"Montserrat",sans-serif;font-weight:500;font-size:36px;line-height:41px;color:var(--white);letter-spacing:1px}
.hero-btn{position:absolute;left:507px;top:352px;width:190px;height:46px;border:2px solid var(--white);color:var(--white);font-family:"Montserrat",sans-serif;font-size:15px;font-weight:600;text-align:center;line-height:42px}
.dots{position:absolute;left:548px;top:580px;display:flex;gap:9px}
.dots span{width:14px;height:14px;border-radius:50%;background:var(--white)}
.dots span.active{background:transparent;border:2px solid var(--white)}

/* about */
.about{top:622px;height:420px;background:var(--white)}
.about-art{position:absolute;left:0;top:0;width:420px;height:420px;background:radial-gradient(circle at 45% 55%,#e9e9e9 0%,#bdbdbd 40%,#f08a3a 70%,#fff 90%)}
.about-title{position:absolute;left:540px;top:74px;font-family:"Montserrat",sans-serif;font-weight:400;font-size:31px;color:var(--ink)}
.about-text{position:absolute;left:540px;top:130px;width:536px;font-size:14px;line-height:27px;color:var(--text)}
.btn{background:var(--blue-dark);color:var(--white);font-family:"Montserrat",sans-serif;font-weight:600;font-size:13px;text-align:center}
.about-btn{position:absolute;left:546px;top:308px;width:137px;height:40px;line-height:40px}

/* support */
.support{top:1042px;height:478px;background:linear-gradient(135deg,#1f8ee0 0%,#1a7fd4 50%,#2a9ae6 100%);overflow:hidden}
.notch{position:absolute;left:563px;top:0;border-left:37px solid transparent;border-right:37px solid transparent;border-top:30px solid var(--white)}
.section-title{position:absolute;left:0;width:1200px;text-align:center;font-family:"Montserrat",sans-serif;font-weight:500}
.support .section-title{top:44px;font-size:27px;color:var(--white)}
.card{position:absolute;top:93px;width:302px;height:347px;background:var(--white)}
.card-img{height:170px;background:linear-gradient(135deg,#0d3c6e,#2f7fc1 60%,#9cc7e6)}
.card h3{margin-top:20px;text-align:center;font-family:"Montserrat",sans-serif;font-weight:500;font-size:19px;color:var(--blue-dark)}
.card p{margin:12px 24px 0;height:54px;overflow:hidden;text-align:center;font-size:12.5px;line-height:18px;color:var(--text)}
.card .more{display:block;text-align:center;margin-top:12px;font-family:"Montserrat",sans-serif;font-size:13px;font-weight:500;color:var(--blue-dark)}
.card .more::after{content:"";display:block;width:22px;height:4px;border-radius:0 0 6px 6px;background:var(--blue-dark);margin:6px auto 0}

/* contact */
.contact{top:1520px;height:320px;background:var(--white)}
.contact .section-title{top:34px;font-size:23px;font-weight:700;color:var(--blue-dark)}
.field{position:absolute;height:45px;border:1px solid var(--line);background:#f6f6f6;font-size:14px;color:var(--text);padding:11px 18px}
.submit{position:absolute;left:533px;top:240px;width:140px;height:36px;line-height:36px}

/* services */
.services{top:1840px;height:507px;background:var(--light);overflow:hidden}
.services .section-title{top:42px;font-size:24px;font-weight:600;color:var(--ink)}
.svc-label{position:absolute;font-size:13.5px;line-height:16px;color:var(--ink);white-space:nowrap}
.svc-brand{position:absolute;left:455px;top:352px;display:flex;align-items:center;gap:10px;font-family:"Montserrat",sans-serif;font-weight:700;font-size:38px;color:#8b8b8b}
.svc-brand span{width:30px;height:30px;background:var(--orange)}

/* testimonials */
.testimonials{top:2347px;height:373px;background:var(--white)}
.testimonials .section-title{top:68px;font-size:23px;color:var(--blue)}
.quote{position:absolute;left:300px;top:136px;width:600px;text-align:center;font-style:italic;font-size:16.5px;line-height:31px;color:var(--text)}
.q-mark{font-family:Georgia,serif;font-style:normal;font-size:36px;color:var(--blue-dark);line-height:0;vertical-align:-8px}
.author{position:absolute;left:0;width:1200px;top:248px;text-align:center;font-size:15px;color:var(--ink)}
.arrow{position:absolute;top:162px}

/* footer */
.site-footer{top:2720px;height:405px;background:linear-gradient(#d0d0d0,#a7a7a7)}
.f-col{position:absolute;top:60px;color:var(--white)}
.f-col h4{font-family:"Montserrat",sans-serif;font-weight:500;font-size:17px;margin-bottom:10px}
.f-col li{list-style:none;font-size:14px;line-height:27px}
.socials{display:flex;gap:8px;margin-top:8px}
.socials span{width:34px;height:34px;border-radius:50%;background:var(--blue);border:2px solid var(--white)}
.f-rule{position:absolute;left:135px;top:302px;width:930px;height:1px;background:rgba(255,255,255,.5)}
.copyright{position:absolute;left:0;width:1200px;top:330px;text-align:center;font-size:12px;color:var(--white)}
</style>
</head>
<body>

<header class="hero">
  <div class="hero-photo" role="img" aria-label="Photo of a hand touching a glowing tablet screen in blue light"></div>
  <div class="brand"><span class="brand-mark"></span>VELMARKETA</div>
  <div class="menu-toggle">
    <svg width="38" height="16" viewBox="0 0 38 16"><g stroke="#fff" stroke-width="2.5"><line x1="0" y1="2" x2="38" y2="2"/><line x1="0" y1="8" x2="38" y2="8"/><line x1="0" y1="14" x2="38" y2="14"/></g></svg>
    MENU
  </div>
  <h1 class="hero-title">FLEXIBLE SOLUTIONS FOR YOUR<br>BUSINESS NEEDS</h1>
  <ul class="nav-drop">
    <li>HOME</li><li>ABOUT US</li><li>SUPPORT</li><li class="has-sub">SERVICES</li><li>PROJECTS</li><li>CONTACT</li>
  </ul>
  <div class="hero-btn">QUICK CONTACT</div>
  <div class="dots"><span class="active"></span><span></span><span></span><span></span></div>
</header>

<section class="about">
  <div class="about-art" role="img" aria-label="Illustration of a silver cube with orange blocks breaking away"></div>
  <h2 class="about-title">About Velmarketa Group, Inc</h2>
  <p class="about-text">Velmarketa is a technology solution provider based in Fairhaven, Ohio. Our goal is to make technology a non-issue for individuals and small to medium size businesses ranging from 5 to 150 Users. Velmarketa has the experience, the tools, high-level technology solutions and training to power your business and your work force. We understand that all business's have one goal in common! (ROI) A Return on Investment</p>
  <div class="btn about-btn">READ MORE</div>
</section>

<section class="support">
  <div class="notch"></div>
  <h2 class="section-title">IT SUPPORT SOLUTIONS</h2>
  <article class="card" style="left:130px">
    <div class="card-img" role="img" aria-label="Photo of a person using a tablet with network graphics"></div>
    <h3>Managed IT Solutions</h3>
    <p>Our staff will design, service, administer and maintain your IT needs. We are well versed on all major operating system, and</p>
    <span class="more">LEARN MORE</span>
  </article>
  <article class="card" style="left:448px">
    <div class="card-img" role="img" aria-label="Photo of a technician working in a server room"></div>
    <h3>Remote Diagnostic</h3>
    <p>Do you need a quick solution to a technical problem? With our live remote-assistance tool, a member of our support team can</p>
    <span class="more">LEARN MORE</span>
  </article>
  <article class="card" style="left:767px">
    <div class="card-img" role="img" aria-label="Photo of an engineer inspecting server racks"></div>
    <h3>IT Infrastructure Design</h3>
    <p>Do you have more than one site? Do you need remote access? We can design and implement LANS/WANS and VPN's.</p>
    <span class="more">LEARN MORE</span>
  </article>
</section>

<section class="contact">
  <h2 class="section-title">QUICK CONTACT FORM</h2>
  <div class="field" style="left:135px;top:90px;width:230px">First Name</div>
  <div class="field" style="left:372px;top:90px;width:230px">Last Name</div>
  <div class="field" style="left:609px;top:90px;width:230px">Email address</div>
  <div class="field" style="left:845px;top:90px;width:230px">Phone</div>
  <div class="field" style="left:135px;top:142px;width:940px;height:83px">Message</div>
  <div class="btn submit">SUBMIT</div>
</section>

<section class="services">
  <h2 class="section-title">OUR SERVICE</h2>
  <svg class="abs" style="left:0;top:0" width="1200" height="507" viewBox="0 0 1200 507">
    <ellipse cx="600" cy="510" rx="382" ry="390" fill="none" stroke="var(--blue)" stroke-width="3"/>
    <g fill="#fff" stroke="#d8d8d8" stroke-width="2">
      <circle cx="220" cy="450" r="24"/><circle cx="247" cy="348" r="24"/><circle cx="302" cy="263" r="24"/>
      <circle cx="383" cy="183" r="24"/><circle cx="540" cy="124" r="24"/><circle cx="693" cy="122" r="24"/>
      <circle cx="843" cy="201" r="24"/><circle cx="918" cy="273" r="24"/><circle cx="960" cy="358" r="24"/><circle cx="980" cy="450" r="24"/>
    </g>
    <g fill="var(--blue)" stroke="var(--blue)">
      <circle cx="220" cy="450" r="8" stroke-width="4" fill="none" stroke-dasharray="3 2"/><circle cx="220" cy="450" r="3"/>
      <circle cx="247" cy="348" r="9"/>
      <line x1="302" y1="255" x2="296" y2="273" stroke-width="2"/><line x1="302" y1="255" x2="308" y2="273" stroke-width="2"/><circle cx="302" cy="255" r="3"/>
      <rect x="373" y="176" width="14" height="14" rx="2"/><path d="M387 183l8-5v10z"/>
      <path d="M540 112v24M530 120l10 6 10-6M532 130l8-4 8 4" fill="none" stroke-width="2"/>
      <rect x="682" y="113" width="22" height="14" fill="none" stroke-width="2.5"/><line x1="688" y1="132" x2="698" y2="132" stroke-width="2"/>
      <g fill="none" stroke-width="2"><circle cx="843" cy="201" r="3"/><line x1="843" y1="201" x2="834" y2="191"/><line x1="843" y1="201" x2="852" y2="191"/><line x1="843" y1="201" x2="834" y2="211"/><line x1="843" y1="201" x2="852" y2="211"/></g>
      <g fill="none" stroke-width="2.5"><path d="M906 271a17 17 0 0 1 24 0"/><path d="M910 276a11 11 0 0 1 16 0"/></g><circle cx="918" cy="281" r="2.5"/>
      <path d="M960 346l10 4v8c0 7-5 11-10 13-5-2-10-6-10-13v-8z"/>
      <path d="M968 456h22a5 5 0 0 0 0-10 8 8 0 0 0-15-2 5 5 0 0 0-7 12z" fill="none" stroke-width="2"/>
    </g>
  </svg>
  <div class="svc-label" style="left:258px;top:436px">Desktop<br>Support</div>
  <div class="svc-label" style="left:287px;top:337px">Network<br>Administration</div>
  <div class="svc-label" style="left:340px;top:258px">Telecommunication</div>
  <div class="svc-label" style="left:415px;top:198px">Audio/video<br>Multimedia</div>
  <div class="svc-label" style="left:530px;top:164px">Disaster<br>Recovery</div>
  <div class="svc-label" style="left:656px;top:168px">Webdesign</div>
  <div class="svc-label" style="left:752px;top:214px">Network<br>Cabling</div>
  <div class="svc-label" style="left:812px;top:280px">Wireless<br>Networks</div>
  <div class="svc-label" style="left:856px;top:352px">Antivirus<br>Solution</div>
  <div class="svc-label" style="left:835px;top:436px">Cloud Hosting<br>Virtualization</div>
  <div class="svc-brand"><span></span>VELMARKETA</div>
</section>

<section class="testimonials">
  <h2 class="section-title">TESTIMONIALS</h2>
  <svg class="arrow" style="left:155px" width="24" height="56" viewBox="0 0 24 56"><path d="M22 2L2 28l20 26" fill="none" stroke="#666" stroke-width="2"/></svg>
  <p class="quote"><span class="q-mark">“</span> Morbi diam mauris viverra in gravida eu mattis in ante Morbi eget arcu Morbi porta libero id ullamcorper nonummy nibh ligula pulvinar metus eget consectetuer augue <span class="q-mark">”</span></p>
  <p class="author">-By Author Name</p>
  <svg class="arrow" style="left:1033px" width="24" height="56" viewBox="0 0 24 56"><path d="M2 2l20 26L2 54" fill="none" stroke="#666" stroke-width="2"/></svg>
</section>

<footer class="site-footer">
  <div class="f-col" style="left:150px"><h4>COMPANY</h4><ul><li>Home</li><li>About Us</li><li>Our Services</li><li>Why Us</li><li>Contact</li></ul></div>
  <div class="f-col" style="left:355px"><h4>RESOURCES</h4><ul><li>Support</li><li>Solutions</li><li>Clients</li><li>Testimonials</li></ul></div>
  <div class="f-col" style="left:560px"><h4>CONTACT INFO</h4><ul><li>415 Alder Park Way Suite B20</li><li>Fairhaven, OH 44210</li><li>(555) 014-2730</li><li>info@velmarketa.com</li></ul></div>
  <div class="f-col" style="left:845px"><h4>FOLLOW US</h4><div class="socials"><span></span><span></span><span></span><span></span></div></div>
  <div class="f-rule"></div>
  <p class="copyright">© 2017 Company Name. All right reserved. Term of Use</p>
</footer>

</body>
</html>
```